Birchline Septic Solutions

Would like to see some single sided ones but would also like to see some double sided with one sided only being the logo. Owners name is Tom Halvick. Phone number is 555-214-0387
Services are pumping, inspections, installs, and repairs

Contact Information for Business Card

555-241-0387 Tom Halvick Fernbrook, OH

```html
<!DOCTYPE html>
<html lang="en">
<head>
<meta charset="utf-8">
<title>Birchline Septic Solutions — Business Card</title>
<link href="https://fonts.googleapis.com/css2?family=Montserrat:wght@500;600;700;800&display=swap" rel="stylesheet">
<style>
  :root {
    --backdrop: #2a2a2c;
    --card-white: #ffffff;
    --ink: #111111;
    --teal: #2bbcb4;
    --rule: #8a8a8a;
    --card-black: #141416;
    --pattern-tone: #26262a;
  }
  * { margin: 0; padding: 0; box-sizing: border-box; }
  html, body { width: 1200px; height: 1108px; overflow: hidden; }
  body {
    background: var(--backdrop);
    font-family: "Montserrat", sans-serif;
    position: relative;
  }
  .card {
    position: absolute;
    top: 184px;
    width: 440px;
    height: 740px;
    border-radius: 28px;
    overflow: hidden;
  }
  .card-front { left: 120px; background: var(--card-white); color: var(--ink); }
  .card-back { left: 640px; background: var(--card-black); }

  .brand-name {
    position: absolute; top: 140px; left: 0; right: 0;
    text-align: center;
    font-weight: 800; font-size: 50px; letter-spacing: 1px;
    line-height: 1.05; text-transform: uppercase;
  }
  .brand-name .tagline {
    display: block; font-size: 19px; font-weight: 500;
    letter-spacing: 7px; margin-top: 10px;
  }

  .holder-name {
    position: absolute; top: 322px; left: 0; right: 0;
    text-align: center; font-weight: 800; font-size: 30px; text-transform: uppercase;
  }
  .contact-row {
    position: absolute; left: 0; right: 0;
    display: flex; align-items: center; justify-content: center; gap: 10px;
  }
  .contact-row .rule { width: 80px; height: 1.5px; background: var(--rule); }
  .contact-row .icon {
    width: 40px; height: 40px; border: 2px solid var(--teal); border-radius: 50%;
    display: flex; align-items: center; justify-content: center;
  }
  .row-phone { top: 395px; }
  .row-place { top: 495px; }
  .contact-text {
    position: absolute; left: 0; right: 0; text-align: center;
    font-weight: 500; font-size: 22px; letter-spacing: 1px;
  }
  .text-phone { top: 446px; }
  .text-place { top: 546px; }

  .services-band {
    position: absolute; left: 0; right: 0; bottom: 0; height: 128px;
    background: var(--teal); color: var(--card-white);
    display: flex; flex-direction: column; align-items: center; justify-content: center;
    font-weight: 600; font-size: 20px; letter-spacing: 1px; line-height: 1.4;
    text-transform: uppercase;
  }

  .back-pattern {
    position: absolute; inset: 0;
    background: linear-gradient(160deg, var(--pattern-tone) 0%, var(--card-black) 70%);
  }
  .back-mark {
    position: absolute; left: 190px; top: 500px;
    display: flex; align-items: center; gap: 8px;
    color: var(--card-white); font-weight: 800; font-size: 26px; text-transform: uppercase;
  }
  .back-mark .dot { width: 12px; height: 12px; background: var(--teal); }
</style>
</head>
<body>
  <section class="card card-front">
    <div class="brand-name">Birchline<span class="tagline">Septic Solutions</span></div>
    <div class="holder-name">Tom Halvick</div>

    <div class="contact-row row-phone">
      <span class="rule"></span>
      <span class="icon">
        <svg width="20" height="20" viewBox="0 0 24 24" fill="none" stroke="#2bbcb4" stroke-width="2.2" stroke-linecap="round" stroke-linejoin="round">
          <path d="M22 16.9v3a2 2 0 0 1-2.2 2 19.8 19.8 0 0 1-8.6-3.1 19.5 19.5 0 0 1-6-6A19.8 19.8 0 0 1 2.1 4.2 2 2 0 0 1 4.1 2h3a2 2 0 0 1 2 1.7c.1.9.4 1.8.7 2.7a2 2 0 0 1-.5 2.1L8 9.8a16 16 0 0 0 6 6l1.3-1.3a2 2 0 0 1 2.1-.4c.9.3 1.8.6 2.7.7a2 2 0 0 1 1.7 2z"/>
        </svg>
      </span>
      <span class="rule"></span>
    </div>
    <div class="contact-text text-phone">555-214-0387</div>

    <div class="contact-row row-place">
      <span class="rule"></span>
      <span class="icon">
        <svg width="20" height="20" viewBox="0 0 24 24">
          <path d="M12 2a7 7 0 0 0-7 7c0 5 7 13 7 13s7-8 7-13a7 7 0 0 0-7-7zm0 9.5A2.5 2.5 0 1 1 12 6.5a2.5 2.5 0 0 1 0 5z" fill="#2bbcb4"/>
        </svg>
      </span>
      <span class="rule"></span>
    </div>
    <div class="contact-text text-place">Fernbrook, OH</div>

    <div class="services-band">
      <span>Pumping • Inspections</span>
      <span>Installs • Repairs</span>
    </div>
  </section>

  <section class="card card-back">
    <div class="back-pattern" role="img" aria-label="Tonal repeating brand pattern on black"></div>
    <div class="back-mark"><span>Birchline</span><span class="dot"></span></div>
  </section>
</body>
</html>
```